RWT Business Cards

We need to design new business cards for our company. We are a Managed Discretionary Account (MDA) adviser based in Sydney Australia. We have distinct corporate colour pallet which will be provided and various logo formats. I will also include our current business card design as a guide only to what we have accepted previously. The final design should convey financial professionalism and experience as well as the necessary company information.

Target Market(s)

High Net Worth and Professional Investors

Industry/Entity Type

Financial

Font styles to use
Serif

```html
<!DOCTYPE html>
<html lang="en">
<head>
<meta charset="utf-8">
<title>RWT Business Cards</title>
<link rel="stylesheet" href="https://fonts.googleapis.com/css2?family=Noto+Sans:wght@700&family=Noto+Serif:wght@400&display=swap">
<style>
  :root {
    --dark-green: #005a0f;
    --card-green: #0b4500;
    --jade: #10a85a;
    --warm-charcoal: #17110d;
    --stone: #a0ab78;
    --black: #000000;
    --white: #ffffff;
    --sans: "Noto Sans", Arial, sans-serif;
    --serif: "Noto Serif", Georgia, serif;
  }
  html, body { margin: 0; padding: 0; overflow: hidden; background: var(--white); }
  .board {
    position: relative; width: 1200px; height: 1000px;
    box-sizing: border-box; border: 2px solid var(--black); background: var(--white);
  }
  .card {
    position: absolute; left: 260px; width: 721px; height: 401px;
    box-sizing: border-box; border: 1.5px solid var(--black); overflow: hidden;
  }
  .palette-card { top: 75px; background: var(--white); }
  .business-card { top: 515px; background: var(--card-green); color: var(--white); font-family: var(--serif); }

  .palette-title {
    position: absolute; left: 24px; top: 28px; margin: 0;
    font: 700 16px var(--sans); letter-spacing: 0.6px; color: var(--black);
  }
  .palette-brand {
    position: absolute; right: 38px; top: 30px; margin: 0;
    font: 700 25px var(--sans); color: var(--dark-green); letter-spacing: 0.3px;
  }
  .swatch {
    position: absolute; left: 236px; right: 0; height: 46px;
    display: flex; align-items: center; padding-left: 17px;
    font: 700 14px var(--sans); letter-spacing: 0.5px; color: var(--white);
  }
  .swatch--dark-green { top: 119px; background: var(--dark-green); }
  .swatch--jade { top: 178px; background: var(--jade); }
  .swatch--charcoal { top: 237px; background: var(--warm-charcoal); }
  .swatch--stone { top: 296px; background: var(--stone); }
  .swatch--black { top: 355px; background: var(--black); }

  .card-rule { position: absolute; left: 10px; top: 18px; }
  .card-brand {
    position: absolute; left: 19px; top: 30px; margin: 0;
    font: 400 33px var(--serif); letter-spacing: 0.2px;
  }
  .holder { position: absolute; left: 0; right: 0; top: 120px; text-align: center; padding-left: 36px; }
  .holder-name { margin: 0; font-size: 40px; line-height: 48px; font-weight: 400; }
  .holder-role { margin: 0; font-size: 24px; line-height: 28px; }
  .address {
    position: absolute; left: 25px; top: 276px; margin: 0; font-style: normal;
    font-size: 20px; line-height: 27px;
  }
  .address .tight { line-height: 25px; }
  .contact {
    position: absolute; right: 19px; top: 248px; margin: 0; padding: 0;
    list-style: none; text-align: right; font-size: 21px; line-height: 36px;
  }
</style>
</head>
<body>
<main class="board">
  <section class="card palette-card" aria-label="RWT colour palette">
    <h2 class="palette-title">RWT COLOUR PALETTE</h2>
    <p class="palette-brand">ROWAN WEST TRUST</p>
    <div class="swatch swatch--dark-green">DARK GREEN - PMS 7484</div>
    <div class="swatch swatch--jade">JADE - PMS 569</div>
    <div class="swatch swatch--charcoal">WARM CHARCOAL - PMS 440</div>
    <div class="swatch swatch--stone">STONE - PMS 7536</div>
    <div class="swatch swatch--black">BLACK</div>
  </section>

  <section class="card business-card" aria-label="Business card">
    <svg class="card-rule" width="4" height="360" viewBox="0 0 4 360" aria-hidden="true">
      <line x1="2" y1="0" x2="2" y2="360" stroke="#ffffff" stroke-width="3" stroke-dasharray="7 5"/>
    </svg>
    <p class="card-brand">ROWAN WEST TRUST</p>
    <div class="holder">
      <h1 class="holder-name">Owen Hartley</h1>
      <p class="holder-role">Managing Director</p>
      <p class="holder-role">Chief Investment Officer</p>
    </div>
    <address class="address">
      <div>Level: 6,22-24 Kent Street</div>
      <div>Sydney NSW 2000</div>
      <div class="tight">Australia</div>
      <div class="tight">www.rowanwest.com.au</div>
    </address>
    <ul class="contact">
      <li>p:1300 555 014</li>
      <li>+61 (0)4 0000 1234</li>
      <li>OWH.@rowanwest.com.au</li>
      <li>Skype: owen.hartley12</li>
    </ul>
  </section>
</main>
</body>
</html>
```